Slick Web Design for Health Care Software Company

We need a new corporate web design for our company, "Brivora." We specialize in web-based cloud software geared toward helping health care professionals.

Our focus for our home site is our products and services. We want potential clients and medical boards who visit our site to have an immediate sense of professionalism and know-how. Our products are innovative, easy to use, and customizable. Users should get this feel when visiting our site.

This is a link to our previous site: www.brivorainc.example. This site is too busy, the colors are too dark, and there's too much information in each page. When creating a design, feel free to eliminate the plethora of info present in the old site.

We have a logo and content for our site that we're going to use. For each of the 7-10 products and services, there is going to be a short 1-2 paragraph excerpt on their own page, as well as a case study related to each. Other parts that can be integrated into the site are our portfolio of clients, newsletter, and about us/contact us.

Some websites to use as general inspiration:
http://www.quellsite.example/
http://www.vantrex.example/
http://www.telmaroplans.example/

Target Market(s)

Health Care Professionals from Specialty Organizations and Boards

Industry/Entity Type

Health Care

Requirements
Nice to have
• Our trademark slogan is "Turn data in knowledge, knowledge into improvement." It would be pretty sweet to integrate this idea into the design of the site.

Also, BE CREATIVE. AVOID TRADITIONAL DESIGNS. Try to exemplify innovation within clarity.
Should not have
• Avoid dark backgrounds.

```html
<!DOCTYPE html>
<html lang="en">
<head>
<meta charset="utf-8">
<title>Brivora — Home</title>
<link href="https://fonts.googleapis.com/css2?family=Anton&family=Archivo+Narrow:wght@700&family=Arimo:wght@400&display=swap" rel="stylesheet">
<style>
  :root {
    --page-bg: #ffffff;
    --capsule-cap: #fde6e4;
    --capsule-body: #f40000;
    --capsule-edge: #3a0000;
    --label-light: #ffffff;
    --ink: #000000;
    --footer-fill: #ff7a77;
    --footer-edge: #e85a57;
    --helix-blue: #5fb8e8;
    --helix-orange: #f2864a;
    --home-top: #fbfbfb;
    --home-bottom: #d9d9d9;
  }
  * { margin: 0; padding: 0; box-sizing: border-box; }
  html, body {
    width: 1200px; height: 930px; overflow: hidden;
    background: var(--page-bg);
  }
  .site {
    position: relative; width: 1200px; height: 930px;
    font-family: "Arimo", Arial, sans-serif;
  }
  .helix-art {
    position: absolute; left: 280px; top: 30px; width: 640px; height: 790px;
    background:
      radial-gradient(ellipse 45% 30% at 45% 22%, rgba(242,134,74,.35), transparent 70%),
      radial-gradient(ellipse 40% 30% at 62% 50%, rgba(95,184,232,.35), transparent 70%),
      radial-gradient(ellipse 35% 30% at 60% 82%, rgba(242,134,74,.3), transparent 70%);
    border-radius: 50%;
  }
  .brand {
    position: absolute; left: 58px; top: 58px;
    display: flex; align-items: center; gap: 12px;
    font-family: "Arimo", Arial, sans-serif; font-size: 44px; color: var(--ink);
  }
  .brand-dot {
    width: 30px; height: 30px; border-radius: 50%; background: #e8e000;
  }
  .capsule {
    position: absolute; width: 129px; height: 337px;
    border-radius: 65px; border: 1.5px solid var(--capsule-edge);
    background: linear-gradient(to bottom, var(--capsule-cap) 0, var(--capsule-cap) var(--split), var(--capsule-body) var(--split), var(--capsule-body) 100%);
    box-shadow: inset -8px 0 14px rgba(0,0,0,.18), inset 8px 0 12px rgba(255,255,255,.35), 2px 3px 6px rgba(0,0,0,.25);
    display: flex; justify-content: center; align-items: flex-end;
    padding-bottom: 14px; text-decoration: none;
  }
  .capsule-label {
    writing-mode: vertical-rl; transform: rotate(180deg);
    font-family: "Anton", Impact, sans-serif; font-size: 38px; line-height: 1;
    color: var(--label-light); letter-spacing: .5px;
  }
  .capsule.is-long { padding-bottom: 8px; }
  .capsule.is-long .capsule-label { font-size: 33px; letter-spacing: 0; }
  .home-button {
    position: absolute; left: 530px; top: 302px; width: 126px; height: 126px;
    border-radius: 50%; border: 1.5px solid #555;
    background: linear-gradient(to bottom, var(--home-top) 0, #eeeeee 48%, #c9c9c9 49%, var(--home-bottom) 100%);
    box-shadow: 2px 3px 6px rgba(0,0,0,.25), inset 0 -8px 12px rgba(0,0,0,.12);
    display: flex; justify-content: center; align-items: center; padding-top: 44px;
    font-family: "Anton", Impact, sans-serif; font-size: 33px; color: var(--ink);
    text-decoration: none;
  }
  .slogan {
    position: absolute; left: 95px; top: 510px; width: 1010px;
    font-family: "Archivo Narrow", "Arial Narrow", sans-serif; font-weight: 700;
    font-size: 48px; color: var(--ink); white-space: nowrap; letter-spacing: -.3px;
  }
  .site-footer {
    position: absolute; left: 55px; top: 812px; width: 1083px; height: 105px;
    background: var(--footer-fill); border: 2px solid var(--footer-edge); border-radius: 4px;
    box-shadow: 0 2px 8px rgba(0,0,0,.3), inset 0 0 10px rgba(180,40,40,.25);
  }
  .footer-nav {
    position: absolute; top: 24px; font-size: 24px; color: var(--ink); white-space: nowrap;
  }
  .footer-nav a { color: var(--ink); text-decoration: none; border-bottom: 1.5px solid var(--ink); }
  .footer-nav.left { left: 71px; }
  .footer-nav.right { left: 635px; }
  .copyright {
    position: absolute; left: 0; right: 0; top: 64px; text-align: center;
    font-size: 23px; color: var(--ink);
  }
</style>
</head>
<body>
<div class="site">
  <div class="helix-art" role="img" aria-label="Illustration of a DNA double helix in blue and orange with coloured base pairs"></div>

  <div class="brand"><span class="brand-dot"></span>Brivora</div>

  <nav class="capsule-nav">
    <a class="capsule" href="#" style="left:138px;top:171px;--split:172px"><span class="capsule-label">ABOUT US</span></a>
    <a class="capsule" href="#" style="left:268px;top:143px;--split:173px"><span class="capsule-label">Services</span></a>
    <a class="capsule" href="#" style="left:399px;top:117px;--split:172px"><span class="capsule-label">Products</span></a>
    <a class="home-button" href="#">Home</a>
    <a class="capsule" href="#" style="left:657px;top:117px;--split:172px"><span class="capsule-label">Resource</span></a>
    <a class="capsule" href="#" style="left:787px;top:145px;--split:173px"><span class="capsule-label">Search</span></a>
    <a class="capsule is-long" href="#" style="left:917px;top:167px;--split:173px"><span class="capsule-label">Contact Us</span></a>
  </nav>

  <h1 class="slogan">Turn Data In Knowledge, Knowledge Into Improvement</h1>

  <footer class="site-footer">
    <div class="footer-nav left"><a href="#">About Us</a> | <a href="#">Services</a> | <a href="#">Products</a></div>
    <div class="footer-nav right"><a href="#">Resources</a> | <a href="#">Search</a> | <a href="#">Contact Us</a></div>
    <p class="copyright">Copy right Brivora Inc. 2013.</p>
  </footer>
</div>
</body>
</html>
```